Design an Outstanding flyer for my company.

I need a flyer designed for our window tinting company based in Brisbane Queensland Australia. The flyer will be targeting Home tinting. We also do mobile car tinting. Something in regards to this could be incorporated into the flyer as well.
I want it to be 2 sided DL size. Black background.
It really needs to Pop, and be a real attention getter.
It needs to be easy to read.
I have provided a mock up with the info on it from our marketing company. It will need a spellcheck etc to make sure everything is correct.
Everything about it can be changed however you like.
I have also included the company logo.

Lets see what you've got!

Target Market(s)

Home Owners

Industry/Entity Type

Home Improvement

Font styles to use
Other font styles liked:
• Duan Penh

Requirements
Must have
• All the information on the mock up. Clear and easy to read.
• Must Stand Out!

```html
<!DOCTYPE html>
<html lang="en">
<head>
<meta charset="utf-8">
<title>Sunvale Tinting – DL Flyer</title>
<link rel="stylesheet" href="https://fonts.googleapis.com/css2?family=PT+Sans:wght@700&display=swap">
<style>
  :root {
    --yellow: #ffff00;
    --black: #000000;
    --white: #ffffff;
    --gold: #f2c200;
    --page: #ffffff;
    --frame: #8a8a8a;
  }
  html, body { margin: 0; padding: 0; overflow: hidden; }
  .canvas {
    position: relative;
    width: 1199px;
    height: 1200px;
    background: var(--page);
    box-sizing: border-box;
    border: 1px solid var(--frame);
    overflow: hidden;
  }
  .flyer {
    position: absolute;
    top: 205px;
    width: 410px;
    height: 787px;
  }
  .flyer--front { left: 173px; }
  .flyer--back { left: 615px; }
  .flyer text {
    font-family: "PT Sans", "Myriad Pro", Arial, sans-serif;
    font-weight: 700;
  }
  .ink-dark { fill: var(--black); }
  .ink-yellow { fill: var(--yellow); }
  .ink-white { fill: var(--white); }
  .ink-gold { fill: var(--gold); }
  .rule-dark { stroke: var(--black); stroke-width: 4; }
  .rule-light { stroke: var(--white); stroke-width: 4; }
</style>
</head>
<body>
<div class="canvas">

  <!-- Front side -->
  <svg class="flyer flyer--front" viewBox="0 0 513 984" aria-label="Flyer front">
    <rect class="ink-yellow" width="513" height="984"/>
    <polygon class="ink-dark" points="513,313 513,984 0,984 0,833"/>

    <g class="headline">
      <text class="ink-dark" x="41" y="103" font-size="60" textLength="444" lengthAdjust="spacingAndGlyphs">KEEP HEAT OUT</text>
      <text class="ink-dark" x="43" y="153" font-size="41" textLength="440" lengthAdjust="spacingAndGlyphs">BLOCK 99.9% UV RAYS</text>
      <text class="ink-dark" x="33" y="220" font-size="72" textLength="460" lengthAdjust="spacingAndGlyphs">SAVE MONEY</text>
      <text class="ink-dark" x="35" y="278" font-size="51" textLength="456" lengthAdjust="spacingAndGlyphs">INCREASE PRIVACY</text>
      <line class="rule-dark" x1="35" y1="288" x2="491" y2="288"/>
    </g>

    <g class="benefits" font-size="13">
      <text class="ink-dark" x="36" y="316" textLength="255" lengthAdjust="spacingAndGlyphs">REDUCE GLARE. REDUCE ENERGY COSTS.</text>
      <text class="ink-dark" x="39" y="337" textLength="363" lengthAdjust="spacingAndGlyphs">CONTROL THE AMOUNT OF LIGHT ENTERING YOUR HOME.</text>
      <text class="ink-dark" x="39" y="357" textLength="386" lengthAdjust="spacingAndGlyphs">REDUCE CARBON FOOTPRINT. MAKE HOME MORE BEAUTIFUL.</text>
      <text class="ink-dark" x="39" y="379" textLength="363" lengthAdjust="spacingAndGlyphs">ELIMINATE HOME HOT SPOTS. PROTECT AGAINST BROKEN</text>
      <text class="ink-dark" x="36" y="399" textLength="328" lengthAdjust="spacingAndGlyphs">GLASS. REGULATE ENERGY. PROTECTS UPHOLSTERY.</text>
      <text class="ink-dark" x="36" y="421" textLength="307" lengthAdjust="spacingAndGlyphs">IMPROVE EFFECTIVENESS OF ROOF INSULATION.</text>
      <text class="ink-dark" x="36" y="441" textLength="289" lengthAdjust="spacingAndGlyphs">IMPROVE HEALTH. REDUCES INTERIOR FLOOR</text>
      <text class="ink-dark" x="36" y="463" textLength="243" lengthAdjust="spacingAndGlyphs">FADING. ELIMINATE NEED FOR BLINDS.</text>
      <text class="ink-dark" x="36" y="483" textLength="197" lengthAdjust="spacingAndGlyphs">STRENGTHEN YOUR WINDOWS.</text>
      <text class="ink-dark" x="36" y="504" textLength="134" lengthAdjust="spacingAndGlyphs">INSULATE IN WINTER.</text>
      <text class="ink-dark" x="36" y="531" font-size="27" textLength="197" lengthAdjust="spacingAndGlyphs">AFFOARDABLE.</text>
      <line class="rule-dark" x1="36" y1="545" x2="240" y2="545"/>
    </g>

    <circle class="ink-gold" cx="413" cy="518" r="38"/>

    <g class="call-to-action">
      <line class="rule-light" x1="280" y1="599" x2="478" y2="599"/>
      <text class="ink-yellow" x="481" y="640" font-size="25" text-anchor="end">20 REASONS WHY</text>
      <text class="ink-yellow" x="481" y="674" font-size="25" text-anchor="end">HOME WINDOW TINTING</text>
      <text class="ink-yellow" x="481" y="709" font-size="25" text-anchor="end">IS PERFECT FOR YOU.</text>
      <text class="ink-white" x="483" y="744" font-size="25" text-anchor="end">CALL BRISBANE’S LEADER IN</text>
      <text class="ink-white" x="483" y="775" font-size="25" text-anchor="end">HOME WINDOW TINTING NOW.</text>
      <text class="ink-yellow" x="173" y="829" font-size="36" textLength="300" lengthAdjust="spacingAndGlyphs">TEL  : 07 3000 4812</text>
      <text class="ink-yellow" x="173" y="861" font-size="36" textLength="300" lengthAdjust="spacingAndGlyphs">SMS : 0400 555 019</text>
      <line class="rule-light" x1="48" y1="879" x2="473" y2="879"/>
    </g>

    <g class="brand">
      <circle class="ink-gold" cx="180" cy="917" r="15"/>
      <text class="ink-gold" x="204" y="925" font-size="21" textLength="150" lengthAdjust="spacingAndGlyphs">SUNVALE TINTING</text>
      <text class="ink-white" x="258" y="953" font-size="10" text-anchor="middle">www.sunvaletinting.com.au</text>
    </g>
  </svg>

  <!-- Back side -->
  <svg class="flyer flyer--back" viewBox="0 0 513 984" aria-label="Flyer back">
    <rect class="ink-yellow" width="513" height="984"/>
    <polygon class="ink-dark" points="513,363 513,984 0,984 0,883"/>

    <g class="intro">
      <text class="ink-dark" x="28" y="71" font-size="37" textLength="311" lengthAdjust="spacingAndGlyphs">20 REASONS WHY</text>
      <text class="ink-dark" x="28" y="106" font-size="37" textLength="436" lengthAdjust="spacingAndGlyphs">HOME WINDOW TINTING</text>
      <text class="ink-dark" x="28" y="140" font-size="37" textLength="371" lengthAdjust="spacingAndGlyphs">IS PERFECT FOR YOU.</text>
      <line class="rule-dark" x1="28" y1="151" x2="484" y2="151"/>
    </g>

    <g class="headline">
      <text class="ink-dark" x="30" y="209" font-size="53" textLength="391" lengthAdjust="spacingAndGlyphs">KEEP HEAT OUT</text>
      <text class="ink-dark" x="34" y="245" font-size="37" textLength="385" lengthAdjust="spacingAndGlyphs">BLOCK 99.9% UV RAYS</text>
      <text class="ink-dark" x="24" y="303" font-size="66" textLength="404" lengthAdjust="spacingAndGlyphs">SAVE MONEY</text>
      <text class="ink-dark" x="26" y="351" font-size="45" textLength="400" lengthAdjust="spacingAndGlyphs">INCREASE PRIVACY</text>
    </g>

    <g class="benefits" font-size="13">
      <text class="ink-dark" x="28" y="371" textLength="255" lengthAdjust="spacingAndGlyphs">REDUCE GLARE. REDUCE ENERGY COSTS.</text>
      <text class="ink-dark" x="31" y="392" textLength="363" lengthAdjust="spacingAndGlyphs">CONTROL THE AMOUNT OF LIGHT ENTERING YOUR HOME.</text>
      <text class="ink-dark" x="31" y="413" textLength="386" lengthAdjust="spacingAndGlyphs">REDUCE CARBON FOOTPRINT. MAKE HOME MORE BEAUTIFUL.</text>
      <text class="ink-dark" x="31" y="434" textLength="363" lengthAdjust="spacingAndGlyphs">ELIMINATE HOME HOT SPOTS. PROTECT AGAINST BROKEN</text>
      <text class="ink-dark" x="28" y="455" textLength="328" lengthAdjust="spacingAndGlyphs">GLASS. REGULATE ENERGY. PROTECTS UPHOLSTERY.</text>
      <text class="ink-dark" x="28" y="476" textLength="307" lengthAdjust="spacingAndGlyphs">IMPROVE EFFECTIVENESS OF ROOF INSULATION.</text>
      <text class="ink-dark" x="28" y="497" textLength="289" lengthAdjust="spacingAndGlyphs">IMPROVE HEALTH. REDUCES INTERIOR FLOOR</text>
      <text class="ink-dark" x="28" y="518" textLength="243" lengthAdjust="spacingAndGlyphs">FADING. ELIMINATE NEED FOR BLINDS.</text>
      <text class="ink-dark" x="28" y="538" textLength="197" lengthAdjust="spacingAndGlyphs">STRENGTHEN YOUR WINDOWS.</text>
      <text class="ink-dark" x="28" y="559" textLength="134" lengthAdjust="spacingAndGlyphs">INSULATE IN WINTER.</text>
      <text class="ink-dark" x="28" y="599" font-size="27" textLength="206" lengthAdjust="spacingAndGlyphs">AFFOARDABLE.</text>
      <line class="rule-dark" x1="28" y1="608" x2="244" y2="608"/>
    </g>

    <circle class="ink-gold" cx="411" cy="648" r="38"/>

    <g class="call-to-action">
      <line class="rule-light" x1="281" y1="714" x2="477" y2="714"/>
      <text class="ink-white" x="482" y="759" font-size="25" text-anchor="end">CALL BRISBANE’S LEADER IN</text>
      <text class="ink-white" x="482" y="789" font-size="25" text-anchor="end">HOME WINDOW TINTING NOW.</text>
      <text class="ink-yellow" x="173" y="829" font-size="36" textLength="301" lengthAdjust="spacingAndGlyphs">TEL  : 07 3000 4812</text>
      <text class="ink-yellow" x="173" y="861" font-size="36" textLength="301" lengthAdjust="spacingAndGlyphs">SMS : 0400 555 019</text>
      <line class="rule-light" x1="48" y1="879" x2="473" y2="879"/>
    </g>

    <g class="brand">
      <circle class="ink-gold" cx="173" cy="917" r="15"/>
      <text class="ink-gold" x="197" y="925" font-size="21" textLength="150" lengthAdjust="spacingAndGlyphs">SUNVALE TINTING</text>
      <text class="ink-white" x="251" y="953" font-size="10" text-anchor="middle">www.sunvaletinting.com.au</text>
    </g>
  </svg>

</div>
</body>
</html>
```